energy rating company

Web Design graphics and layout only

To create two pages for the website. First the home page and the second is the design for the job board for our clients use after login. I have attached files that explain in detail what the pages should have and the purpose/desires of each object. Please read these thoroughly.

The webpages need to be clean, professional, easy on the eye, obvious in all its buttons and functions with a strong call to action on the home page and branding and clean, great and obvious looking buttons and very simple but dynamic as well. We wish to be seen as contemporary.

Business Concept

Our business concept is simple, to build a website whereby our clients will be able to upload jobs for energy raters to quote on and subsequent complete the work if their quote is selected. To link energy ratings that are required with energy raters via our website. Similarly to the varlo website, jobs will be “advertised” on the job board and raters will select which jobs they wish to quote for.

I have attached a Word document explaining all the parts of the website and another word document showing what we are sort of after and a excel spreadsheet as well. Please read these in conjunction with this brief!
Updates

Dear All

I have submitted with my brief a word doc and excel spreadsheet of the two pages I want created.  However this is not the layout or design I want, I only put it together so that you will need to know what is required on each page.  Feel free to change and redesign it all.

Also the second page does not require the "process" logo or any other menu items except the first five being Home, How it works, About Us, testimonials and Contact us as per the home page.

We also are looking for something very professional and very clean.  It should be very easy to see exactly what you are looking for.

I will also extend the deadline for new designers!!  I am excited to see your talents!!

Thanks

I have increase budget and posted a note saying feel free to change all the details layout etc on my brief just include everything!!! 

Wanting a professional corporate look...

Want a professional corporate look

We have changed our minds and you we no longer require the process to be on the home page.

Thanks

Target Market(s)

Target Market

Home Inspection Companies
Pest Inspection Companies
Residential home buyers/sellers
Real Estate companies

Industry/Entity Type

It Company

Number of Pages Required

1 page

Requirements
Must have
• Colours and Styles

• The website should be mainly white as I believe it is seen as clean and simple with colour from the logos, but can be swayed if it projects the image we are after.

• It should be obvious and process orientated and I do believe symbols, pictures, etc should replace words where possible.

```html
<!DOCTYPE html>
<html lang="en">
<head>
<meta charset="utf-8">
<title>voltra australia – Energy Rating Quotes</title>
<link href="https://fonts.googleapis.com/css2?family=Source+Sans+3:ital,wght@0,400;0,600;0,700;1,400&display=swap" rel="stylesheet">
<style>
:root{
  --orange:#c25a0e;
  --green:#2e9a1f;
  --green-dark:#1f8a16;
  --green-top:#7cc21c;
  --green-bottom:#4aa818;
  --grey-band:#ececec;
  --page-bg:#f3f3f3;
  --text:#555;
  --nav:#555;
  --card:#ebebeb;
}
*{margin:0;padding:0;box-sizing:border-box}
html,body{width:984px;height:1200px;overflow:hidden}
body{background:var(--page-bg);font-family:"Source Sans 3",sans-serif;color:var(--text);position:relative}
.abs{position:absolute}
.brand{left:92px;top:58px;font-size:30px;font-weight:600;color:var(--orange);line-height:1}
.account-links{left:806px;top:76px;font-size:11px;color:var(--green)}
.account-links span{color:var(--orange)}
.page-panel{left:29px;top:137px;width:926px;height:963px;background:#fff;border-radius:12px;box-shadow:0 1px 6px rgba(0,0,0,.25);overflow:hidden}
.nav{font-size:14px;color:var(--nav)}
.nav a{text-decoration:none;color:inherit;position:absolute;white-space:nowrap}
.nav a.active{font-weight:700;color:#444}
.search{left:702px;top:15px;width:153px;height:28px;border-radius:14px;background:#fff;box-shadow:inset 0 1px 4px rgba(0,0,0,.3)}
.search svg{position:absolute;left:9px;top:6px}
.band{left:0;top:67px;width:926px;height:208px;background:var(--grey-band)}
.tab{top:0;width:127px;height:53px;border-radius:0 0 8px 8px;background:linear-gradient(var(--green-bottom),var(--green-top));color:#fff;font-size:13.5px;text-align:center;display:flex;align-items:center;justify-content:center;line-height:1.3;box-shadow:0 2px 3px rgba(0,0,0,.2)}
.step{color:var(--green);font-style:italic;font-size:19px;text-align:center;line-height:1.25;transform:translate(-50%,-50%)}
.step-arrow{transform:translate(-50%,-50%)}
.content{font-size:14px;line-height:1.3}
.intro{left:67px;top:308px;width:600px}
.intro b{font-weight:400;color:var(--orange);font-size:19px}
.headline{left:67px;top:366px;width:585px;font-size:22px;line-height:1.27;color:var(--orange)}
.cta{left:64px;top:461px;width:641px;height:51px;border-radius:9px;background:linear-gradient(var(--green-top),var(--green-bottom));color:#fff;font-size:13.5px;display:flex;align-items:center;justify-content:center}
.cta em{font-style:normal;font-size:18px}
.register{left:67px;top:544px;width:620px;font-size:14px}
.checks{list-style:none;left:97px;font-size:13.5px;font-style:italic;color:var(--green)}
.checks li{height:23px;display:flex;align-items:center;gap:7px}
.checks li svg{flex:none}
.closing{left:67px;top:868px;width:600px;font-size:14px;line-height:1.3}
.closing b{font-weight:400;color:var(--orange);font-size:19px}
.card{background:var(--card);border-radius:10px}
.card h2{font-weight:400;color:var(--orange);font-size:19px;position:absolute;left:8px;top:10px}
.login{left:701px;top:294px;width:155px;height:156px}
.field-label{font-size:10px;color:#555;position:absolute;text-align:right;width:50px}
.field{position:absolute;left:59px;width:88px;height:16px;border-radius:8px;background:#fff;box-shadow:inset 0 1px 3px rgba(0,0,0,.25)}
.login-btn{position:absolute;left:79px;top:110px;width:68px;height:16px;border-radius:8px;background:var(--orange);color:#fff;font-size:10px;text-align:center;line-height:16px}
.testimonials{left:701px;top:462px;width:155px;height:432px}
.t-item{position:absolute;left:8px;width:118px;height:46px;border-bottom:1px solid #d3d3d3;display:flex;gap:6px}
.t-item .name{color:var(--green);font-size:12.5px;line-height:1.1;margin-top:3px}
.t-item .meta{color:#999;font-size:6px}
.scroll{position:absolute;left:142px;top:42px;width:3px;height:370px;background:#ddd;border-radius:2px}
.scroll::before{content:"";position:absolute;left:-3px;top:6px;width:9px;height:9px;border-radius:50%;background:#e4e4e4}
.footer-nav a{top:1127px;font-size:14px}
.copyright{left:643px;top:1129px;font-size:11px;font-style:italic;color:#555}
</style>
</head>
<body>

<div class="abs brand">voltra australia</div>
<div class="abs account-links">Log in <span>| Register</span></div>

<div class="abs page-panel">
  <nav class="nav">
    <a class="active" style="left:64px;top:23px">Home</a>
    <a style="left:119px;top:23px">How it works?</a>
    <a style="left:216px;top:23px">About Us</a>
    <a style="left:290px;top:23px">Testimonials</a>
    <a style="left:385px;top:23px">Contact Us</a>
    <a style="left:470px;top:23px">Help</a>
  </nav>
  <div class="abs search">
    <svg width="16" height="16" viewBox="0 0 16 16"><circle cx="6" cy="6" r="4.5" fill="none" stroke="#ccc" stroke-width="1.5"/><line x1="9.5" y1="9.5" x2="14" y2="14" stroke="#ccc" stroke-width="2"/></svg>
  </div>

  <section class="abs band">
    <div class="abs tab" style="left:445px">Get a quote</div>
    <div class="abs tab" style="left:589px">Energy Raters<br>Add your busines</div>
    <div class="abs tab" style="left:728px">Active<br>Job Board</div>

    <div class="abs step" style="left:113px;top:129px">Post a Job</div>
    <div class="abs step" style="left:287px;top:129px">Get As many<br>Quotes<br>as you like</div>
    <div class="abs step" style="left:460px;top:129px">Select<br>Energy<br>Quote<br>that suits</div>
    <div class="abs step" style="left:636px;top:129px">Approve<br>Payment</div>
    <div class="abs step" style="left:806px;top:129px">Receive<br>Rating</div>

    <svg class="abs step-arrow" style="left:200px;top:133px" width="34" height="40" viewBox="0 0 34 40"><path d="M4 2 C4 18 10 24 20 24 L20 16 L32 28 L20 40 L20 32 C8 32 2 22 4 2 Z" fill="var(--green-dark)"/></svg>
    <svg class="abs step-arrow" style="left:374px;top:133px" width="34" height="40" viewBox="0 0 34 40"><path d="M4 2 C4 18 10 24 20 24 L20 16 L32 28 L20 40 L20 32 C8 32 2 22 4 2 Z" fill="var(--green-dark)"/></svg>
    <svg class="abs step-arrow" style="left:547px;top:133px" width="34" height="40" viewBox="0 0 34 40"><path d="M4 2 C4 18 10 24 20 24 L20 16 L32 28 L20 40 L20 32 C8 32 2 22 4 2 Z" fill="var(--green-dark)"/></svg>
    <svg class="abs step-arrow" style="left:720px;top:133px" width="34" height="40" viewBox="0 0 34 40"><path d="M4 2 C4 18 10 24 20 24 L20 16 L32 28 L20 40 L20 32 C8 32 2 22 4 2 Z" fill="var(--green-dark)"/></svg>
  </section>

  <p class="abs content intro"><b>voltra australia</b> is Australia's leading professional energy rating consultancy firm specializing in large scaled residential and commercial energy rating logistics.</p>
  <p class="abs headline">We have professional and accredited energy raters in all States and Territories ready and waiting to provide quotes for and per-form&nbsp; your energy rating jobs!</p>
  <div class="abs cta">It's&nbsp;<em>Free</em>,&nbsp;<em>Fast</em>&nbsp;and&nbsp;<em>Easy</em>&nbsp;to use and you get the best price and turnaround time that suits you!!</div>
  <p class="abs register">Register with us, upload your job and specifications, and sit back and watch as energy raters provide quotes for your work!</p>

  <ul class="abs checks" style="top:591px">
    <li><svg width="10" height="9" viewBox="0 0 10 9"><path d="M1 5 L4 8 L9 1" fill="none" stroke="var(--green)" stroke-width="2"/></svg>Get the best priced quotes for your energy ratings</li>
    <li><svg width="10" height="9" viewBox="0 0 10 9"><path d="M1 5 L4 8 L9 1" fill="none" stroke="var(--green)" stroke-width="2"/></svg>Save time by listing a job to get many quotes</li>
    <li><svg width="10" height="9" viewBox="0 0 10 9"><path d="M1 5 L4 8 L9 1" fill="none" stroke="var(--green)" stroke-width="2"/></svg>Monitor your jobs and quotes on your own job board</li>
  </ul>
  <ul class="abs checks" style="top:683px">
    <li><svg width="10" height="9" viewBox="0 0 10 9"><path d="M1 5 L4 8 L9 1" fill="none" stroke="var(--green)" stroke-width="2"/></svg>Be notified via email of all new quotes as they come in</li>
    <li><svg width="10" height="9" viewBox="0 0 10 9"><path d="M1 5 L4 8 L9 1" fill="none" stroke="var(--green)" stroke-width="2"/></svg>Be able to specify your dturnaround times</li>
    <li><svg width="10" height="9" viewBox="0 0 10 9"><path d="M1 5 L4 8 L9 1" fill="none" stroke="var(--green)" stroke-width="2"/></svg>Accessible anytime and anywhere</li>
    <li><svg width="10" height="9" viewBox="0 0 10 9"><path d="M1 5 L4 8 L9 1" fill="none" stroke="var(--green)" stroke-width="2"/></svg>Choose a deadline for energy raters to supply quotes</li>
    <li><svg width="10" height="9" viewBox="0 0 10 9"><path d="M1 5 L4 8 L9 1" fill="none" stroke="var(--green)" stroke-width="2"/></svg>Have access to many qualified energy raters in your state all quoting for your work</li>
    <li><svg width="10" height="9" viewBox="0 0 10 9"><path d="M1 5 L4 8 L9 1" fill="none" stroke="var(--green)" stroke-width="2"/></svg>Be able to track your jobs and pay online</li>
    <li><svg width="10" height="9" viewBox="0 0 10 9"><path d="M1 5 L4 8 L9 1" fill="none" stroke="var(--green)" stroke-width="2"/></svg>Provide feedback on energy raters</li>
  </ul>

  <p class="abs closing">Its <b>totally free to be registered</b> with us and there is no obligations or hidden catches!&nbsp; So if you wish to utilise the amazing opportunity register now!&nbsp; This new website will be going live on the (insert date) so be ready to <b>save some money!</b></p>

  <aside class="abs card login">
    <h2>Login area</h2>
    <span class="field-label" style="left:2px;top:58px">Email</span>
    <div class="field" style="top:56px"></div>
    <span class="field-label" style="left:2px;top:84px">Password</span>
    <div class="field" style="top:82px"></div>
    <div class="login-btn">Login</div>
  </aside>

  <aside class="abs card testimonials">
    <h2>Testimonials</h2>
    <div class="scroll"></div>
    <div class="t-item" style="top:42px"><svg width="31" height="31" viewBox="0 0 31 31" role="img" aria-label="Testimonial author photo"><rect x=".5" y=".5" width="30" height="30" fill="#fff" stroke="#333"/><path d="M1 1 L30 30 M30 1 L1 30" stroke="#333"/></svg><div><div class="name">Testimonial 1</div><div class="meta">25.03.2010 | 12 comments</div></div></div>
    <div class="t-item" style="top:88px"><svg width="31" height="31" viewBox="0 0 31 31" role="img" aria-label="Testimonial author photo"><rect x=".5" y=".5" width="30" height="30" fill="#fff" stroke="#333"/><path d="M1 1 L30 30 M30 1 L1 30" stroke="#333"/></svg><div><div class="name">Testimonial 2</div><div class="meta">25.03.2010 | 12 comments</div></div></div>
    <div class="t-item" style="top:134px"><svg width="31" height="31" viewBox="0 0 31 31" role="img" aria-label="Testimonial author photo"><rect x=".5" y=".5" width="30" height="30" fill="#fff" stroke="#333"/><path d="M1 1 L30 30 M30 1 L1 30" stroke="#333"/></svg><div><div class="name">Testimonial 3</div><div class="meta">25.03.2010 | 12 comments</div></div></div>
    <div class="t-item" style="top:180px"><svg width="31" height="31" viewBox="0 0 31 31" role="img" aria-label="Testimonial author photo"><rect x=".5" y=".5" width="30" height="30" fill="#fff" stroke="#333"/><path d="M1 1 L30 30 M30 1 L1 30" stroke="#333"/></svg><div><div class="name">Testimonial 4</div><div class="meta">25.03.2010 | 12 comments</div></div></div>
    <div class="t-item" style="top:226px"><svg width="31" height="31" viewBox="0 0 31 31" role="img" aria-label="Testimonial author photo"><rect x=".5" y=".5" width="30" height="30" fill="#fff" stroke="#333"/><path d="M1 1 L30 30 M30 1 L1 30" stroke="#333"/></svg><div><div class="name">Testimonial 5</div><div class="meta">25.03.2010 | 12 comments</div></div></div>
    <div class="t-item" style="top:272px"><svg width="31" height="31" viewBox="0 0 31 31" role="img" aria-label="Testimonial author photo"><rect x=".5" y=".5" width="30" height="30" fill="#fff" stroke="#333"/><path d="M1 1 L30 30 M30 1 L1 30" stroke="#333"/></svg><div><div class="name">Testimonial 6</div><div class="meta">25.03.2010 | 12 comments</div></div></div>
    <div class="t-item" style="top:318px"><svg width="31" height="31" viewBox="0 0 31 31" role="img" aria-label="Testimonial author photo"><rect x=".5" y=".5" width="30" height="30" fill="#fff" stroke="#333"/><path d="M1 1 L30 30 M30 1 L1 30" stroke="#333"/></svg><div><div class="name">Testimonial 7</div><div class="meta">25.03.2010 | 12 comments</div></div></div>
    <div class="t-item" style="top:364px;border-bottom:none"><svg width="31" height="31" viewBox="0 0 31 31" role="img" aria-label="Testimonial author photo"><rect x=".5" y=".5" width="30" height="30" fill="#fff" stroke="#333"/><path d="M1 1 L30 30 M30 1 L1 30" stroke="#333"/></svg><div><div class="name">Testimonial 7</div><div class="meta">25.03.2010 | 12 comments</div></div></div>
  </aside>
</div>

<nav class="nav footer-nav">
  <a class="active" style="left:93px">Home</a>
  <a style="left:148px">How it works?</a>
  <a style="left:245px">About Us</a>
  <a style="left:319px">Testimonials</a>
  <a style="left:414px">Contact Us</a>
  <a style="left:499px">Help</a>
</nav>
<div class="abs copyright">Copyright © 2010 voltra australia. All rights reserved.</div>

</body>
</html>
```